Flyer

I am a qualified accountant and I need a flyer to promote my business when networking

My services include
Management Accounts, Financial Accounts, Day to Day Bookkeeping services, business start up assistance
I will produce and submit Self Assessment Tax Returns, Annual Accounts, VAT tax returns, Payroll and PAYE

I attach my business card design so that there is some continuity if you think it appropiate.

Size A3 is preferred, please.

Sorry, I mean't Size A5 is preferred.

A5 please

Free initial consultations and advice.

```html
<!DOCTYPE html>
<html lang="en">
<head>
<meta charset="utf-8">
<title>Clara Moss Accounting – Flyer</title>
<link rel="stylesheet" href="https://fonts.googleapis.com/css2?family=Cinzel:wght@500;700&family=Source+Sans+3:wght@400;600;700&family=Crimson+Text:ital@1&family=Oswald:wght@700&display=swap">
<style>
  :root {
    --page: #e9e9e4;
    --lime: #c3d83a;
    --lime-light: #d8e874;
    --lime-deep: #abc42a;
    --green: #0f6b33;
    --olive: #4e5c12;
    --ink: #222;
    --white: #fff;
  }
  * { margin: 0; padding: 0; box-sizing: border-box; }
  html, body { width: 932px; height: 1200px; overflow: hidden; background: var(--page); }
  .flyer {
    position: absolute; left: 123px; top: 84px; width: 686px; height: 1031px;
    background: radial-gradient(ellipse at 60% 45%, var(--lime-light) 0%, var(--lime) 45%, var(--lime-deep) 100%);
    overflow: hidden; font-family: "Source Sans 3", sans-serif;
    box-shadow: 0 6px 20px rgba(0,0,0,.25);
  }
  .texture {
    position: absolute; left: 0; right: 0; top: 240px; height: 520px;
    background: linear-gradient(160deg, rgba(255,255,255,0) 20%, rgba(255,255,255,.16) 50%, rgba(255,255,255,0) 80%);
  }
  .centered { position: absolute; left: 0; width: 100%; text-align: center; }
  .brand { top: 146px; }
  .brand-name {
    font-family: "Cinzel", serif; font-weight: 500; font-size: 37px; line-height: 44px;
    color: var(--green); display: inline-flex; align-items: center; gap: 12px; white-space: nowrap;
  }
  .brand-dot { width: 14px; height: 14px; border-radius: 50%; background: var(--green); }
  .tagline { font-size: 23px; line-height: 30px; color: var(--green); }
  .photo-back {
    position: absolute; left: 290px; top: 330px; width: 170px; height: 195px;
    background: linear-gradient(135deg, #2f6db5, #a4cbee); border: 6px solid var(--white);
    transform: rotate(9deg); box-shadow: 0 4px 10px rgba(0,0,0,.3);
  }
  .photo {
    position: absolute; left: 240px; top: 345px; width: 190px; height: 215px;
    border: 9px solid var(--white); transform: rotate(-12deg);
    background: linear-gradient(160deg, #c9b89a, #8b6b4c 60%, #4a3a33);
    box-shadow: 0 6px 14px rgba(0,0,0,.35);
  }
  .person { top: 578px; }
  .person-name { font-family: "Cinzel", serif; font-weight: 700; font-size: 29px; line-height: 36px; color: var(--ink); }
  .person-role { font-size: 24px; line-height: 30px; font-weight: 700; color: var(--white); }
  .services-band {
    position: absolute; left: 30px; top: 760px; width: 626px; height: 140px;
    background: var(--olive); border-radius: 0 0 14px 14px;
  }
  .consult {
    top: 866px; font-family: "Crimson Text", serif; font-style: italic; font-size: 19px; line-height: 24px; color: var(--lime-light);
  }
  .services {
    position: absolute; left: 30px; top: 688px; width: 626px; height 172px; height: 172px;
    background: linear-gradient(#fff, #eceee8); border-radius: 14px;
    box-shadow: 0 3px 8px rgba(0,0,0,.25); padding: 38px 14px 0 34px;
  }
  .services-title {
    position: absolute; left: 165px; top: -20px; width: 296px; height: 42px;
    background: var(--green); color: var(--white); font-weight: 700; font-size: 25px;
    text-align: center; line-height: 42px;
  }
  .service-list { list-style: none; display: grid; grid-template-columns: 346px 1fr; row-gap: 10px; }
  .service-list li { display: flex; align-items: flex-start; gap: 12px; font-size: 17px; line-height: 24px; color: var(--ink); white-space: nowrap; }
  .service-list li.wide { grid-column: 1 / 3; }
  .service-list svg { flex: none; width: 20px; height: 20px; margin-top: 2px; }
  .wide span { text-align: center; }
  .email { top: 912px; font-size: 24px; line-height: 30px; font-weight: 700; color: var(--white); }
  .call {
    top: 946px; font-family: "Oswald", sans-serif; font-weight: 700; font-size: 56px; line-height: 70px;
    color: var(--white); text-shadow: 0 3px 4px rgba(0,0,0,.35); white-space: nowrap;
  }
  .call-label { font-family: "Cinzel", serif; font-size: 40px; }
</style>
</head>
<body>
<main class="flyer">
  <div class="texture"></div>

  <header class="brand centered">
    <div class="brand-name"><span class="brand-dot"></span>Clara Moss Accounting</div>
    <p class="tagline">Making Accounts look easy</p>
  </header>

  <div class="photo-back" role="img" aria-label="Printed card with blue design behind the portrait"></div>
  <div class="photo" role="img" aria-label="Portrait photograph of the accountant"></div>

  <section class="person centered">
    <h1 class="person-name">Clara Moss ACMA, CGMA</h1>
    <p class="person-role">Qualified Accountant</p>
  </section>

  <div class="services-band"></div>
  <p class="consult centered">Free initial consultations and advice</p>

  <section class="services">
    <h2 class="services-title">My services include</h2>
    <ul class="service-list">
      <li><svg viewBox="0 0 18 18"><rect x="1" y="3" width="14" height="14" fill="#fff" stroke="#0f6b33" stroke-width="1.5"/><path d="M4 9l3 4 9-11" fill="none" stroke="#0f6b33" stroke-width="2.5"/></svg>Management Accounts</li>
      <li><svg viewBox="0 0 18 18"><rect x="1" y="3" width="14" height="14" fill="#fff" stroke="#0f6b33" stroke-width="1.5"/><path d="M4 9l3 4 9-11" fill="none" stroke="#0f6b33" stroke-width="2.5"/></svg>Financial Accounts</li>
      <li><svg viewBox="0 0 18 18"><rect x="1" y="3" width="14" height="14" fill="#fff" stroke="#0f6b33" stroke-width="1.5"/><path d="M4 9l3 4 9-11" fill="none" stroke="#0f6b33" stroke-width="2.5"/></svg>Day to Day Bookkeeping Services</li>
      <li><svg viewBox="0 0 18 18"><rect x="1" y="3" width="14" height="14" fill="#fff" stroke="#0f6b33" stroke-width="1.5"/><path d="M4 9l3 4 9-11" fill="none" stroke="#0f6b33" stroke-width="2.5"/></svg>business start up assistance</li>
      <li class="wide"><svg viewBox="0 0 18 18"><rect x="1" y="3" width="14" height="14" fill="#fff" stroke="#0f6b33" stroke-width="1.5"/><path d="M4 9l3 4 9-11" fill="none" stroke="#0f6b33" stroke-width="2.5"/></svg><span>I will produce and submit Self Assessment Tax Returns, Annual Accounts,<br>VAT tax returns, Payroll and PAYE</span></li>
    </ul>
  </section>

  <p class="email centered">clara@claramossaccounting.com</p>
  <p class="call centered"><span class="call-label">Call :</span> 07700 900482</p>
</main>
</body>
</html>
```